Lantern Petals Website v.1 - attract floral shop franchisees

I need a simple information website for my new business. We are a franchisor of flower shops. The overall purpose of the website is to promote the company and the service, especially to potential franchisees and retailers. Only about 4 pages are required including homepage, About, For Supermarkets, For Franchisees, and Contact. No special functions are required except the site will have two separate inquiry forms that must be filled out online and submitted via automated email. Similarly, an email form should be linked from the Contact page. I have a logo and business cards designed by CraftHarbor, and I would like the site to have a consistent color scheme and style. The key to design will be to express the joy and love associated with flowers and floral bouquets.
IMPORTANT - I will be exporting the website design to Pageloft CMS in a site hosted by NetMarlow. For smooth integration into PageLoft hosted by NetMarlow, the designer should build the site using a PageLoft-friendly format. Ideally, they should use HTML, CSS, and PHP. Creating a custom theme or using a page builder that exports to PageLoft-compatible files is best. This ensures the site can be easily imported and managed within PageLoft.

Target Market(s)

Potential franchisees (existing florists or creative types who might like to own a floral business) and supermarkets who might want us to run their floral department

Industry/Entity Type

Floral retailing

Coding

Coded - Design and coding required

Number of Pages Required

4 page

Requirements
Must have
• A brand theme that is beautiful, consistent throughout and builds on the logo design
Nice to have
• Show gender and ethnic diversity in customers and florists. Pictures of happy florists (for franchisees) and pictures of amazing floral department displays (for supermarkets)

```html
<!DOCTYPE html>
<html lang="en">
<head>
<meta charset="UTF-8">
<title>Lantern Petals</title>
<link rel="stylesheet" href="https://fonts.googleapis.com/css2?family=Pinyon+Script&family=Poppins:wght@400;500&display=swap">
<style>
:root{
  --pink:#f5e6e6;
  --orange:#f0ac2c;
  --green:#33a05f;
  --sky:#dce8ea;
  --card:#f4f4f4;
  --ink:#1c1c1c;
  --text:#6a6a6a;
  --white:#ffffff;
  --bee-soft:#e3efe2;
}
*{margin:0;padding:0;box-sizing:border-box}
html,body{width:1200px;height:3489px;overflow:hidden}
body{position:relative;background:var(--white);font-family:'Poppins',sans-serif;color:var(--text)}
.abs{position:absolute}
.script{font-family:'Pinyon Script',cursive;color:var(--ink);font-weight:400}
.btn{position:absolute;display:flex;align-items:center;justify-content:center;background:var(--orange);color:var(--ink);border-radius:22px;font-size:13px;letter-spacing:3px;text-transform:uppercase;font-weight:500}
.nav a{position:absolute;top:57px;font-size:13px;letter-spacing:3px;color:var(--ink);text-decoration:none;text-transform:uppercase}
.brand{left:27px;top:40px;display:flex;align-items:center;gap:10px;font-size:22px;color:var(--orange);font-weight:500}
.brand-dot{width:34px;height:34px;border-radius:50%;background:var(--green)}
.hero-title{left:54px;top:200px;font-size:66px}
.hero-copy{left:54px;top:289px;width:500px;font-size:14px;line-height:20.5px}
.photo{position:absolute}
.bee-art{position:absolute;border-radius:18px;background:linear-gradient(160deg,#dcebd9 0%,var(--bee-soft) 60%,rgba(255,255,255,0) 100%)}
.about-title{left:562px;top:890px;font-size:54px}
.about-copy{left:559px;top:970px;width:545px;font-size:13px;line-height:20px}
.about-copy p+p{margin-top:20px}
.snow{left:4px;top:1479px;width:1196px;height:705px;background:var(--sky)}
.snow-title{left:127px;top:1722px;font-size:54px}
.snow-copy{left:129px;top:1806px;width:540px;font-size:17px;line-height:25.2px}
.badge{left:141px;top:2019px;width:76px;height:74px;background:#e6dcd6}
.card{position:absolute;top:2356px;width:470px;height:253px;background:var(--card)}
.card h3{position:absolute;left:38px;top:22px;font-size:50px}
.card p{position:absolute;left:36px;top:94px;width:380px;font-size:15px;line-height:22px}
.card .btn{left:37px;top:183px;width:151px;height:40px}
.foot-title{font-size:44px}
.foot-links a{position:absolute;left:100px;font-size:14px;letter-spacing:3px;color:var(--ink);text-decoration:none;text-transform:uppercase}
.contact-line{position:absolute;left:359px;display:flex;align-items:center;gap:14px;font-size:15px;color:var(--ink)}
.icon{width:38px;height:38px;border-radius:50%;border:1.5px solid var(--green);display:flex;align-items:center;justify-content:center}
.newsletter{left:670px;top:3017px;width:451px;height:275px;background:var(--white)}
.field{position:absolute;left:26px;top:113px;width:280px;height:50px;border:1px solid #555;border-radius:25px;padding-left:34px;display:flex;align-items:center;font-size:14px;color:#777;background:var(--white);z-index:1}
.subscribe{position:absolute;left:26px;top:186px;width:280px;height:49px;border-radius:25px;background:var(--green);color:var(--white);display:flex;align-items:center;justify-content:center;font-size:16px;letter-spacing:4px;z-index:1}
.rule{left:100px;top:3381px;width:1013px;height:1px;background:#c9bcbc}
.copyright{left:0;top:3418px;width:1122px;text-align:center;font-size:14px;color:var(--ink)}
</style>
</head>
<body>

<svg class="abs" style="left:0;top:0" width="1200" height="800" viewBox="0 0 1200 800">
  <path fill="var(--pink)" d="M0,0 H1200 V690 C900,740 600,700 400,640 C250,595 100,585 0,590 Z"/>
  <path fill="var(--orange)" d="M0,590 C100,585 250,595 400,640 C600,700 900,740 1200,690 L1200,700 C1000,760 750,750 580,735 C400,715 200,670 0,677 Z"/>
  <path fill="var(--green)" d="M0,690 C200,670 420,700 582,735 C400,712 200,705 0,785 Z"/>
</svg>

<header class="nav">
  <div class="abs brand"><span class="brand-dot"></span>Lantern Petals</div>
  <a style="left:272px">Home</a>
  <a style="left:368px">About</a>
  <a style="left:479px">For Supermarkets</a>
  <a style="left:724px">For Franchisees</a>
  <div class="btn" style="left:980px;top:45px;width:150px;height:39px">Contact</div>
</header>

<section class="hero">
  <h1 class="abs script hero-title">Lantern Petals</h1>
  <p class="abs hero-copy">Fresh flowers convey beauty and love, and in our view should become something every person regularly enjoys. Lantern Petals is an entrepreneurial company created to make top quality fresh flowers and professionally-designed bouquets accessible to every consumer at affordable prices.</p>
  <div class="btn" style="left:54px;top:427px;width:152px;height:40px">Contact</div>
  <div class="photo" role="img" aria-label="Pink and white gerbera daisies with palm leaves in a speckled pink pot" style="left:600px;top:110px;width:560px;height:560px;border-radius:48% 48% 40% 40%;background:radial-gradient(circle at 50% 40%,#f7b8c8 0%,#f3d2d9 45%,rgba(245,230,230,0) 72%)"></div>
</section>

<section class="about">
  <div class="bee-art" role="img" aria-label="Illustration of a small bee with its looping flight trail" style="left:150px;top:815px;width:100px;height:190px"></div>
  <svg class="abs" role="img" aria-label="Honeycomb collage of roses, hydrangeas and greenery photographs" style="left:68px;top:900px" width="433" height="480" viewBox="0 0 433 480">
    <defs><polygon id="hexA" points="78,0 39,67 -39,67 -78,0 -39,-67 39,-67"/></defs>
    <g transform="translate(218,235) rotate(-22)">
      <use href="#hexA" transform="translate(135,-78)" fill="#e7eddc"/>
      <use href="#hexA" transform="translate(135,78)" fill="#dfe8cf"/>
      <use href="#hexA" transform="translate(0,156)" fill="#b0244f"/>
      <use href="#hexA" transform="translate(-135,78)" fill="#2f5a2b"/>
      <use href="#hexA" transform="translate(-135,-78)" fill="#cbd6a6"/>
      <use href="#hexA" transform="translate(0,-156)" fill="#9c9aa6"/>
    </g>
  </svg>
  <h2 class="abs script about-title">About</h2>
  <div class="abs about-copy">
    <p>Professional florists typically sell the finest quality stems, design the most beautiful bouquets and provide the finest customer service, but their costs – of floral products, retail spaces, labor and marketing – force them to pass high prices along to customers. Supermarket flower departments benefit from high customer footfall, economies of scale and low pricing, but their quality of stems and bouquets is typically poor, staffing is limited, and staff turnover is high which can result in inefficiency, wastage, poorly merchandised selections and limited service.</p>
    <p>Lantern Petals brings the best of professional florists and supermarkets together for the benefit of consumers. It supports a national network of owner-operator franchisees, who in many cases are multi-site professional florists, with comprehensive services to enhance franchise profitability. Lantern Petals works with some of the country's largest and most progressive supermarkets to provide franchisee ownership and operation of their strategically important floral departments. Supermarkets find that Lantern Petals is able to improve their financial outcomes, provide attentive customer service and satisfaction, and lift the quality of the entire store environment.</p>
  </div>
  <div class="btn" style="left:559px;top:1339px;width:151px;height:40px">Contact</div>
</section>

<section class="abs snow">
  <div class="photo" role="img" aria-label="Pink gerbera daisies and rosebuds with green leaves" style="left:23px;top:8px;width:240px;height:190px;border-radius:50%;background:radial-gradient(circle,#f1a7bd 0%,#e9c4cc 45%,rgba(220,232,234,0) 72%)"></div>
</section>
<h2 class="abs script snow-title">Frostline</h2>
<p class="abs snow-copy">Lantern Petals operates in partnership with Frostline Group, the leading franchisor of sushi stations and pre-packaged fruit &amp; vegetable departments to supermarkets across the United States and United Kingdom. Lantern Petals' combination of floral and supermarket franchising expertise guarantees that consumers, franchisees and supermarket partners each receive exceptional service and value.</p>
<div class="abs badge"></div>
<svg class="abs" role="img" aria-label="Honeycomb collage of fruit skewers, chocolate fountain and food station photographs" style="left:731px;top:1649px" width="409" height="406" viewBox="0 0 409 406">
  <defs><polygon id="hexB" points="68,0 34,59 -34,59 -68,0 -34,-59 34,-59"/></defs>
  <g transform="translate(205,203) rotate(-22)">
    <use href="#hexB" transform="translate(118,-68)" fill="#8a5228"/>
    <use href="#hexB" transform="translate(118,68)" fill="#3c4a4c"/>
    <use href="#hexB" transform="translate(0,136)" fill="#2a2a24"/>
    <use href="#hexB" transform="translate(-118,68)" fill="#d3b13a"/>
    <use href="#hexB" transform="translate(-118,-68)" fill="#c9a534"/>
    <use href="#hexB" transform="translate(0,-136)" fill="#b7bcc4"/>
  </g>
</svg>

<section class="services">
  <div class="bee-art" role="img" aria-label="Illustration of a small bee with its looping flight trail" style="left:27px;top:2281px;width:82px;height:180px"></div>
  <div class="bee-art" role="img" aria-label="Illustration of a small bee with its looping flight trail" style="left:1090px;top:2288px;width:82px;height:180px"></div>

  <div class="card" style="left:107px">
    <h3 class="script">For Supermarkets</h3>
    <p>Lantern Petals works with some of the country's largest and most progressive supermarkets to provide franchisee ownership</p>
    <div class="btn">Read More</div>
  </div>
  <div class="card" style="left:626px">
    <h3 class="script">For Franchisee</h3>
    <p>Lantern Petals works with some of the country's largest and most progressive supermarkets to provide franchisee ownership</p>
    <div class="btn">Read More</div>
  </div>
</section>

<svg class="abs" style="left:0;top:2700px" width="1200" height="789" viewBox="0 0 1200 789">
  <path fill="var(--pink)" d="M0,175 C300,190 700,140 1200,80 V789 H0 Z"/>
  <path fill="var(--orange)" d="M0,130 C300,175 700,110 1200,35 V90 C800,110 400,200 0,175 Z"/>
  <path fill="var(--green)" d="M610,178 C800,140 1000,125 1200,128 V238 C1100,180 900,160 610,178 Z"/>
</svg>

<footer>
  <h3 class="abs script foot-title" style="left:77px;top:3018px">About</h3>
  <nav class="foot-links">
    <a style="top:3114px">Home</a>
    <a style="top:3161px">About</a>
    <a style="top:3208px">For Supermarkets</a>
    <a style="top:3258px">For Franchisee</a>
    <a style="top:3307px">Contact</a>
  </nav>

  <h3 class="abs script foot-title" style="left:363px;top:3018px">Contact</h3>
  <div class="contact-line" style="top:3107px">
    <span class="icon"><svg width="18" height="18" viewBox="0 0 24 24"><path fill="var(--green)" d="M6.6 10.8a15.1 15.1 0 0 0 6.6 6.6l2.2-2.2a1 1 0 0 1 1-.25 11.4 11.4 0 0 0 3.6.57 1 1 0 0 1 1 1V20a1 1 0 0 1-1 1A17 17 0 0 1 3 4a1 1 0 0 1 1-1h3.5a1 1 0 0 1 1 1c0 1.25.2 2.45.57 3.6a1 1 0 0 1-.25 1z"/></svg></span>
    +1 555 010 4826
  </div>
  <div class="contact-line" style="top:3166px">
    <span class="icon"><svg width="18" height="18" viewBox="0 0 24 24"><rect x="3" y="6" width="18" height="13" rx="2" fill="var(--green)"/><path d="M3.5 7l8.5 6 8.5-6" fill="none" stroke="#fff" stroke-width="1.6"/></svg></span>
    info@Lantern-Petals.com
  </div>

  <div class="abs newsletter">
    <h3 class="abs script foot-title" style="left:45px;top:28px">Newsletter</h3>
    <div class="field">Email Address</div>
    <div class="subscribe">SUBSCRIBE NOW</div>
    <div class="photo" role="img" aria-label="Bouquet of pink peonies and roses in a pale blue jug" style="left:300px;top:57px;width:151px;height:218px;background:radial-gradient(circle at 55% 35%,#eaa9bf 0%,#e8d6d9 45%,rgba(255,255,255,0) 75%)"></div>
  </div>

  <div class="abs rule"></div>
  <p class="abs copyright">Copyright 2024 Lantern Petals. All Rights Reserved.</p>
</footer>

</body>
</html>
```